Tradeshow Booth, Banners & Brochure Design

Corvin Meridian (www.corvinmeridian.example) is a Veltrax Partner specializing in developing products and customizations for Veltrax Ledgerline QP. The purpose of this project is to develop a unified approach to graphic design for our tradeshow booth, banners and product literature. This should result in completed designs for the booth and banners, and several templates that can be used to create our product literature.

***WE WILL ONLY LOOK THROUGH THE FIRST 100 SUBMISSIONS***
Updates

Reason: We have received some requests for an extended deadline, and we would like to encourage more submissions, so we are extending the deadline by two days. Please let us know if you have any questions or need clarification on our design brief.

Thanks for the submissions and questions everyone.  I will get answers to your questions, and more detailed specs, posted within the next couple of hours.  I will also provide detailed feedback to your designs within that time.

Q:  How large should each item be – what is the approximate number of words/lines, columns/rows?

 

-          We have updated the Content Type list to cut it down and simplify this.  For word count, we are attaching the text for our NEW brochure on WMS, which we intend to be a 4 page brochure.  We have labeled each section according to content type.  This can be used as a guide for how much text each content area must be able to accommodate.  You can even pull the raw text straight from the word file for your design.  The CCEM brochure, already included, is an OLD brochure, and represents a design that we are trying to evolve beyond.

 

-          Keep in mind that the 4 page product brochure will be a 17” by 11” single sheet, folded.  The 2 page product brochure will be a single 8.5” by 11” sheet, printed on both sides.

 

-          For the 2 page product brochure, assume something that looks like half of the 4 page design.  For example, we will be creating one brochure for “Financials” which comprises two products.  Product A will go on the front, and Product B on the back.  We will still need to allow for contact information and the other content types as specified.

 

-          For the 4 page corporate overview, we have attached our current corporate overview for reference, and labeled the content types.  Again, feel free to pull raw text directly from this for purposes of your design – though remember, this OLD brochure represents a design we are trying to evolve beyond.

 

-          For images (screenshots, stock photography, diagrams, etc) we are thinking we would like to see about 4 on the 4 page brochure, but only 1-2 for the 2 page brochure.  The corporate overview can have suitable imagery at your discretion.

 

-          We would like to see some of the imagery used in the Tradeshow materials (booth, banners) carried across to the brochures.

 

 

 

Q:  What are the detailed print guidelines, especially in relation to bleeds, etc?

 

-          For all the brochures, use a full bleed.  If your design incorporates a bleed of color across a fold, try to have the bleed going across no more than 25% of the height of the page.  CMYK color, 300DPI, 8.5”w x 11”h.  We will most likely go with 100# paper without too much gloss on it. 

 

-          For all other materials such as booth and banners, no bleeds.  Please see specification sheets for the booth and banners, included below.  Create your designs to the exact size given.

 

 

 

Q:  Will booth graphics be printed as one continuous piece, or will they be applied in sections that are in line with the panel dimensions of the 8 center panels and end caps?

 

-          Graphics are printed as one continuous piece on a large format printer.  They are then cut into the individual panel pieces for shipping and storage.  When the booth is fully assembled, the seams are hardly noticeable unless you are looking for them from a short distance away.

 

-          We are already in possession of one 10’ booth, and will be ordering another, with the associated pieces, to create the 20’ booth.  The booth comprises a support structure, and the actual graphics panels which are attached to the front.  The overall 20’ design should take into account the fact that we will, in the future, attend tradeshows with only a 10’ booth, so only half of the panels will be used.  We would like to be able to mix and match our four categories to suit the show.

Reason: We are extending the deadline one more time to allow Tamsin and anyone else who needs the extra time for the brochure design.

Please prioritize your brochure design at this time.  We are interested in receiving feedback on deadlines - if you can confirm that you will submit a design but need more time to do so, we would like to hear from you.

Reason: To provide time for solid designs from all the designers who have been invited, we are extended the deadline one more time. This will be the final extension.

Target Market(s)

Corporate Clients

Industry/Entity Type

Graphic Design

Requirements
Must have
• TRADESHOW SPECIFIC
1. Graphics for 10'x20' “Heronfold” Tradeshow Booth
a. Layout should approximate the grid we have mocked up in our preliminary layout – see below. There is a fair amount of flexibility so long as the basic grid, contents and dimensions are adhered to.

2. Graphics needed for 3 retractable banner stands
a. Two banner stands will have dimensions of 24” x 88”
b. The third banner stand will have dimensions of 36” x 88” and will be double-sided. The design for this banner should have the option to be scaled down to 33.5” wide, for a possible additional banner stand being considered.
c. Banners should approximate what is shown in the preliminary layout – see below.
d. All banner stands being used are able to fully extend to 92”- however, the height of the booth itself is 88” and we would like all tradeshow specific elements to be the same height.

PRODUCT LITERATURE
1. Graphic Design and Layout needed for brochures:
a. double-sided one page for Products
b. double-sided two page for Products
c. double-sided two page for Overview

2. Pages would be full bleed letter size 8.5” x 11.

3. Samples are included below to get an idea of common grids and layouts for similar publications, as well as one of our current publications for reference.

4. Product literature must include provisions for all of the content types listed in that document, included below. There is some leeway with image placement – a product brochure doesn’t necessarily have to have stock photos, diagrams, AND software screenshots.

5. The designer will need to indicate what specs are required for software screenshots so that we can generate appropriate files for that use.

COMMON ELEMENTS
• Images need to include stock photos of people in business settings, as well as stock photos related to warehousing, barcoding systems, and supply chains. Other images to be used should include schematics, workflow diagrams, and other items that are related to the areas in which the company works. Each heading on the booth, and each page on the brochures, will need one image at minimum. Images and content laid out next to each other should be thematically related whenever possible. We will also create a small number of simple diagrams in house that will need to be redesigned and recreated in the appropriate format and placed in the designs.
• Clean, high-impact design. The Veltrax Tabular Bookkeeping brochure, included below, is a good example of this.
• Our current logo, included below, needs to have the tagline removed. We are also requesting that a different version of the graphic element in the logo be created, in monochrome but with roughly the same geometry.
• Our new tagline is “Integrated Solutions for Ledgerline QP” but it should not be located directly in the logo area as our current tagline is, “Making systems business-ready”.
• Designs should be produced in print-ready PDF files. We will be using Kestrel Layout Pro R4 to open the PDF files, drop in our copy and other content, and finalize the designs. The PDF files will then be sent directly to our booth production and brochure printing companies.

```html
<!DOCTYPE html>
<html lang="en">
<head>
<meta charset="utf-8">
<title>Corvin360 WMS – Receiving &amp; Inventory Management</title>
<link rel="stylesheet" href="https://fonts.googleapis.com/css2?family=Libre+Franklin:wght@700;800&family=Arimo:wght@400&family=Source+Sans+3:ital,wght@0,400;0,600;1,400&display=swap">
<style>
  :root {
    --page-bg: #e6e7e9;
    --panel-bg: #d9d9e0;
    --band: #8886b8;
    --band-soft: #cfcde0;
    --intro: #fdc98a;
    --intro-soft: #fbe0bd;
    --heading: #5e5c9c;
    --ink: #222326;
    --white: #ffffff;
    --placeholder-a: #b9b6d3;
    --placeholder-b: #e9e8ef;
  }
  * { box-sizing: border-box; margin: 0; padding: 0; }
  html, body { width: 940px; height: 1200px; overflow: hidden; }
  body {
    position: relative;
    background: var(--page-bg);
    font-family: "Source Sans 3", "Myriad Pro", sans-serif;
    color: var(--ink);
  }
  .section-backdrop {
    position: absolute; left: 66px; width: 794px;
    background: var(--panel-bg);
  }
  .section-title {
    position: absolute; left: 80px; width: 767px; height: 38px;
    background: var(--band);
    color: var(--white);
    font-family: "Libre Franklin", "Franklin Gothic Medium", sans-serif;
    font-weight: 800; font-size: 20px; letter-spacing: .6px;
    line-height: 38px; padding-left: 13px;
  }
  .intro-edge {
    position: absolute; left: 66px; width: 14px;
    background: var(--intro-soft);
  }
  .intro {
    position: absolute; left: 80px; width: 243px;
    background: var(--intro);
    font-family: "Arimo", Arial, sans-serif;
    font-size: 16.4px; line-height: 20.8px;
    padding: 17px 20px 0 13px;
  }
  .content {
    position: absolute; left: 323px; width: 524px;
    background: var(--white);
  }
  .col { position: absolute; width: 240px; }
  .feature h3 {
    font-family: "Libre Franklin", "Franklin Gothic Medium", sans-serif;
    font-weight: 800; font-size: 14px; line-height: 20px;
    color: var(--heading); letter-spacing: .3px;
    text-transform: uppercase; margin-bottom: 6px;
  }
  .feature p { font-size: 13.3px; line-height: 17.4px; hyphens: auto; -webkit-hyphens: auto; }
  .feature + .feature { margin-top: 16px; }
  .media {
    position: absolute;
    background: linear-gradient(160deg, var(--placeholder-b), var(--placeholder-a));
  }
  .media.screenshot { border: 1px solid #9a9aa6; }
  .media.diagram { background: linear-gradient(160deg, #f4f4f6, #d7d7dc); }
  .testimonial { position: absolute; left: 80px; top: 996px; width: 767px; }
  .testimonial h2 {
    font-family: "Libre Franklin", "Franklin Gothic Medium", sans-serif;
    font-weight: 800; font-size: 19px; color: var(--heading);
    letter-spacing: .3px; line-height: 24px; margin-bottom: 2px;
  }
  .testimonial blockquote { font-style: italic; font-size: 11.8px; line-height: 17.6px; }
  .testimonial .cite {
    text-align: right; margin-top: 14px; margin-right: 13px;
    font-size: 13px; line-height: 17.6px; color: var(--heading);
  }
  .testimonial .cite strong { font-weight: 600; display: block; }
</style>
</head>
<body>

<section class="section receiving">
  <div class="section-backdrop" style="top:94px;height:407px"></div>
  <h2 class="section-title" style="top:106px">RECEIVING</h2>
  <div class="intro-edge" style="top:144px;height:357px"></div>
  <p class="intro" style="top:144px;height:357px">Does receiving inventory take too long that your sales department has no idea what is available? Connect your front office with your warehouse and increase your sales potential by receiving inventory in real-time.</p>
  <div class="content" style="top:144px;height:343px"></div>
  <div class="col" style="left:336px;top:156px">
    <div class="feature">
      <h3>Automatic Validation</h3>
      <p>Inventory is automatically validated against an existing purchase order in Veltrax Ledgerline QP and can be viewed via barcode scanners. The barcode scanning interface also uses Veltrax Ledgerline QP rules and item configuration to display appropriate information and prompts at all times. This allows for easy training amongst warehouse staff.</p>
    </div>
    <div class="feature">
      <h3>Organized Warehouse and Productive Staff</h3>
      <p>Warehouse items can be received into a default Receiving Bin where staff can easily transfer them to their appropriate location via Bin-to-Bin Transfer.</p>
    </div>
  </div>
  <div class="col" style="left:592px;top:156px">
    <div class="feature">
      <h3>Streamlined Bulk Receiving</h3>
      <p>By simply importing vendor shipment data files into the Bulk Receiving Module, you can generate Purchase Receipt data and print inventory labels for multiple items to help expedite the process of receiving large shipments.</p>
    </div>
  </div>
  <div class="media screenshot" role="img" aria-label="Software screenshot of the bulk receiving module" style="left:592px;top:306px;width:242px;height:152px"></div>
</section>

<section class="section inventory">
  <div class="section-backdrop" style="top:545px;height:406px"></div>
  <h2 class="section-title" style="top:560px">INVENTORY MANAGEMENT</h2>
  <div class="intro-edge" style="top:598px;height:353px"></div>
  <p class="intro" style="top:598px;height:353px">Do you dread the time it takes to do an inventory stock count? With Corvin360 WMS you can not only reduce the time it takes to complete a count, but minimize the errors by using barcode scanners instead of pen and paper.</p>
  <div class="content" style="top:598px;height:353px"></div>
  <div class="col" style="left:336px;top:608px">
    <div class="feature">
      <h3>Accurate Site and Bin Tracking</h3>
      <p>Perform Site-to-Site inventory transfer or Bin-to-Bin moves while maintaining a complete log of all transfer transactions. Corvin360 WMS also supports bin transfers of items on un-posted PO Receipts so you’re always “in the know”.</p>
    </div>
    <div class="feature">
      <h3>Timely Stock Counts</h3>
      <p>Process timely and relevant stock counts via barcode scanners utilizing the Stock Count Schedule in Veltrax Ledgerline QP. Warehouse supervisors can also setup Stock Count Schedules based on bin locations, sites or other filters for extreme effectiveness.</p>
    </div>
  </div>
  <div class="media diagram" role="img" aria-label="Illustration of a workflow diagram with boxes and arrows" style="left:595px;top:608px;width:229px;height:168px"></div>
</section>

<aside class="testimonial">
  <h2>WHAT CORVIN360 WMS USERS HAVE TO SAY:</h2>
  <blockquote>“Linden Row Food Service has been using Corvin Meridian’s barcoding system for several years. It has given us the controls and efficiencies that we need. Rafael and his team delivered several enhancements to Veltrax Ledgerline QP which have significantly improved our sales order entry process, shipment routing, and handling of catch-weight items. I certainly recommend Corvin Meridian’s services and products to any company that uses Veltrax Ledgerline QP.”</blockquote>
  <p class="cite"><strong>Marcus T. President</strong>Linden Row Food Service</p>
</aside>

</body>
</html>
```